Webiste Design KDW

Design the website using uploaded content. Design colors should match that of the company logo with an allowance of one more extra color if it makes the website look much better and colorful. Use Technology related stock images in your design.

Target Market(s)

Potential Clients - Companies

Industry/Entity Type

Information Technology

Coding

Coded - Design and coding required

Number of Pages Required

5+ page

Requirements
Must have
• Company Logo Colors
Nice to have
• Professional Look and Feel with Sliders showing professional information technology images

```html
<!DOCTYPE html>
<html lang="en">
<head>
<meta charset="utf-8">
<title>KDW Technologies</title>
<link href="https://fonts.googleapis.com/css2?family=Montserrat:wght@400;500;700;800&family=Roboto:wght@300;400&display=swap" rel="stylesheet">
<style>
  :root{
    --orange:#ff9412;
    --orange-deep:#ff8a00;
    --ink:#111111;
    --white:#ffffff;
    --hero-a:#1a2a6e;
    --hero-b:#7a3b8f;
    --hero-c:#2aa8e0;
    --hero-d:#0b1240;
    --panel:rgba(110,100,110,0.55);
    --peach:#fde6cf;
  }
  *{margin:0;padding:0;box-sizing:border-box}
  html,body{width:1200px;height:675px;overflow:hidden;background:var(--white)}
  body{position:relative;font-family:'Roboto',Arial,sans-serif;color:var(--ink)}

  .topbar{position:absolute;left:0;top:0;width:1200px;height:89px;background:var(--orange)}
  .brand{position:absolute;left:431px;top:0;width:337px;height:89px;background:var(--white);
    display:flex;align-items:center;justify-content:center;gap:10px}
  .brand-dot{width:22px;height:22px;border-radius:50%;background:var(--orange-deep)}
  .brand-name{font-family:'Montserrat',sans-serif;font-weight:800;font-size:30px;color:var(--orange-deep);letter-spacing:1px;line-height:1}

  .navrow{position:absolute;left:0;top:89px;width:1200px;height:33px;background:var(--white)}
  .contact-mail{position:absolute;left:17px;top:8px;font-family:'Montserrat',sans-serif;font-size:15px;color:var(--ink)}
  .contact-phone{position:absolute;right:17px;top:10px;font-family:'Montserrat',sans-serif;font-size:15px;color:var(--ink)}
  .mainnav{position:absolute;left:312px;top:6px;display:flex;gap:17px;list-style:none}
  .mainnav li{font-size:19px;color:var(--orange);line-height:1}

  .substrip{position:absolute;left:0;top:122px;width:1200px;height:28px;background:var(--orange-deep)}
  .subnav{position:absolute;left:382px;top:0;width:436px;height:23px;background:var(--white);
    border-radius:0 0 5px 5px;display:flex;justify-content:space-around;align-items:center;list-style:none;font-size:15px}

  .hero{position:absolute;left:0;top:150px;width:1200px;height:346px;
    background:
      radial-gradient(ellipse 300px 80px at 1050px 150px, rgba(130,220,255,0.7), transparent 70%),
      radial-gradient(ellipse 420px 200px at 520px 120px, rgba(190,80,170,0.6), transparent 70%),
      linear-gradient(100deg, var(--hero-a) 0%, var(--hero-b) 40%, var(--hero-c) 75%, var(--hero-d) 100%)}
  .hero-panel{position:absolute;left:56px;top:143px;width:872px;height:176px;background:var(--panel);padding:6px 11px}
  .hero-title{font-family:'Montserrat',sans-serif;font-weight:700;font-size:43px;line-height:56px;color:var(--orange)}
  .hero-text{font-family:'Roboto',sans-serif;font-weight:300;font-size:24px;line-height:26px;color:var(--white);margin-top:2px}

  .about{position:absolute;left:0;top:496px;width:1200px;height:179px;
    background:
      radial-gradient(circle 160px at 80px 120px, var(--peach), transparent 75%),
      radial-gradient(circle 160px at 1110px 120px, var(--peach), transparent 75%),
      var(--white)}
  .about-title{position:absolute;left:0;width:1237px;top:28px;text-align:center;
    font-family:'Montserrat',sans-serif;font-weight:500;font-size:37px;color:var(--orange);letter-spacing:1px}
  .about-copy{position:absolute;left:189px;top:90px;width:857px;font-family:Arial,sans-serif;font-size:14px;line-height:15px;
    text-align:justify;text-align-last:center}
  .about-copy p+p{margin-top:15px}
</style>
</head>
<body>
  <header class="topbar">
    <div class="brand"><span class="brand-dot"></span><span class="brand-name">KDW TECHNOLOGIES</span></div>
  </header>

  <nav class="navrow">
    <span class="contact-mail">info@kdwtech.co.za</span>
    <ul class="mainnav">
      <li>Home</li><li>About Us</li><li>Services</li><li>Solutions</li><li>Clients</li><li>Offices</li><li>Contact</li>
    </ul>
    <span class="contact-phone">087-555-0142</span>
  </nav>

  <div class="substrip">
    <ul class="subnav"><li>Managed Services</li><li>Hosting Services</li><li>Transportation</li></ul>
  </div>

  <section class="hero" role="img" aria-label="Technology network photograph with glowing nodes and connecting lines in blue and purple">
    <div class="hero-panel">
      <h1 class="hero-title">Most innovative and preferred<br>ICT and Engineering Company</h1>
      <p class="hero-text">KDW Technologies is committed to the fair and ethical treatment<br>of employees and stakeholders</p>
    </div>
  </section>

  <section class="about" role="img" aria-label="Soft peach network pattern behind the company introduction">
    <h2 class="about-title">Thought Behind KDW</h2>
    <div class="about-copy">
      <p>KDW Technologies was founded in 2013 as a Private Company. For Most of its initial existence, the company intends to establish close relationships with its various clients, with the intension of expanding throughout South Africa. KDW Technologies is dedicated to leveraging emerging technologies to provide the highest level of quality products and services, customer service, and security.</p>
      <p>Our Company is built on the assumption that the management of information technology for business is like legal advice or accounting.</p>
    </div>
  </section>
</body>
</html>
```